Bref créative |
Website preferably Joomla template. | ||
Network and IT consulting. | ||
Information Technology | ||
http://quorinnetworks.com | ||
Quorin Networks has been established with the goal of becoming a recognizable brand, as a company which provides complex information technology solutions for enterprise organizations and service providers. Our services will include design and implementation of Local Area and Wide Area networks, IPv6 implementation solutions and strategies, Voice over IP, Data Center design, Server virtualization and consolidation, Wireless, and more. The initial rendition of the Quorin networks website needs to convey the technical advancement of Quorin networks, through graphics and some animation. However, the initial website will remain relatively simple in content, consisting predominantly of static content. Some flash animation may be used at a later time. To keep things simple going forward Quorin Networks would like to use Joomla to manage it’s content. A front end joomla template would be preferred but not required to ensure the site still presents a professional image. | ||
We dislike looks that are to creative and hard to distinguish. | ||
Clean/Simple Content Driven Conservative Corporate Modern Service Oriented High Tech |
Orage | ||
left side | ||
http://www.brellmarket.com/ | ||
http://www.tovanix.ca/ | ||
http://www.mireldo.com/ | ||
Please base this on our logo appearance. http://dl.hovrabin.com/u/572031/Quorin_ok.png |

```html
<!DOCTYPE html>
<html lang="en">
<head>
<meta charset="utf-8">
<title>Quorin Networks — Keeping customers happy</title>
<link href="https://fonts.googleapis.com/css2?family=Source+Sans+3:ital,wght@0,400;0,600;0,700;1,700&display=swap" rel="stylesheet">
<style>
:root{
  --orange:#e8922e;
  --orange-dark:#c8701a;
  --orange-light:#f2ad55;
  --panel:#e9e9e9;
  --panel-line:#d2d2d2;
  --white:#ffffff;
  --blue:#2b6f9e;
  --text:#555555;
  --cream:#fbe6c8;
}
*{margin:0;padding:0;box-sizing:border-box}
html,body{width:1200px;height:1078px;overflow:hidden}
body{font-family:"Source Sans 3",Arial,sans-serif;color:var(--text);position:relative;
  background:radial-gradient(ellipse at 40% 40%,var(--orange-light) 0%,var(--orange) 45%,var(--orange-dark) 100%)}
.abs{position:absolute}

/* header */
.brand{left:58px;top:70px;display:flex;align-items:center;gap:14px}
.brand-mark{width:22px;height:22px;background:var(--white)}
.brand-name{font-size:34px;font-weight:600;color:var(--white);line-height:1}
.brand-tag{left:58px;top:112px;font-size:15px;color:var(--cream)}
.nav-item{top:190px;color:var(--white)}
.nav-item h2{font-size:32px;font-style:italic;font-weight:700;line-height:1}
.nav-item p{font-size:14px;color:var(--cream)}
.server-photo{left:845px;top:15px;width:300px;height:262px;background:linear-gradient(135deg,#3a3a3a,#0e0e0e);border-radius:4px 4px 0 0}

/* middle band */
.plans{left:0;top:277px;width:364px;height:343px;background:var(--panel)}
.plan{height:114px;border-bottom:1px solid var(--panel-line);padding:38px 0 0 30px;position:relative}
.plan h3{font-size:24px;color:var(--blue);font-weight:400;line-height:1.1}
.plan h3 i{font-weight:700}
.plan p{font-size:14px;color:var(--text)}
.order{position:absolute;left:248px;top:40px;width:94px;height:32px;background:var(--white);border:1px solid #bdbdbd;font-size:14px;color:#333;display:flex;align-items:center;justify-content:center;gap:8px}
.order svg{width:18px;height:18px}

.center{left:364px;top:277px;width:446px;height:620px;background:var(--white);box-shadow:0 0 12px rgba(0,0,0,.15)}
.feature{height:114px;border-bottom:1px solid #e2e2e2;display:flex;align-items:center;padding-left:40px}
.feature .thumb{width:62px;height:72px;background:linear-gradient(135deg,#c8c8c8,#4a4a4a);border-radius:4px;margin-right:40px}
.feature p{font-size:16px;line-height:1.3;color:var(--text)}
.news{padding:26px 0 0 40px}
.news h3{font-size:30px;color:var(--blue);font-weight:400}
.news .date{font-size:13px;margin-top:40px;color:var(--text)}
.news h4{font-size:21px;color:var(--blue);font-weight:400;margin-top:2px}
.news p{font-size:16px;line-height:1.3;margin-top:8px;width:320px}

.upgrades{left:810px;top:277px;width:390px;height:343px;background:var(--panel);padding:30px 0 0 44px}
.upgrades h3{font-size:32px;color:var(--blue);font-weight:400;line-height:1}
.upgrades .sub{font-size:13px;color:#333;margin-top:4px}
.rack{width:180px;height:26px;margin-top:24px;background:linear-gradient(180deg,#d8d8d8,#8a8a8a);border-radius:2px}
.upgrades .body{font-size:16px;line-height:1.3;margin-top:46px;width:300px}

/* lower band */
.access{left:30px;top:640px}
.access h3{font-size:25px;font-weight:400;color:var(--blue);line-height:1}
.access .sub{font-size:13px;color:var(--cream)}
.lock{left:265px;top:624px;width:48px;height:60px;background:linear-gradient(135deg,#f3d57a,#b58a1e);border-radius:6px}
.field{left:30px;width:230px;height:26px;background:var(--white);border:1px solid #d0a060;font-size:13px;color:#888;padding:4px 8px}
.login{left:30px;top:800px;width:80px;height:30px;background:#f4f4f4;border:1px solid #c89060;font-size:14px;color:#333;display:flex;align-items:center;justify-content:center}
.forgot{left:30px;top:850px;font-size:13px;color:var(--blue);text-decoration:underline}

.links{left:810px;top:620px;width:390px}
.link{height:88px;border-bottom:1px solid rgba(255,255,255,.35);padding:24px 0 0 44px;position:relative}
.link h3{font-size:25px;color:var(--white);font-weight:400;line-height:1}
.link p{font-size:13px;color:var(--cream)}
.link svg{position:absolute;right:22px;top:32px;width:22px;height:22px}

/* footer */
.footer{left:0;top:980px;width:1200px;display:flex;justify-content:space-between;padding:0 50px;font-size:13px;color:var(--white)}
.footer small{display:block;font-size:10px;color:var(--cream)}
.footer nav{display:flex;gap:24px}
</style>
</head>
<body>

<header>
  <div class="abs brand">
    <span class="brand-mark"></span>
    <span class="brand-name">Quorin Networks</span>
  </div>
  <div class="abs brand-tag">keeping customers happy</div>
  <div class="abs nav-item" style="left:58px"><h2>About Us.</h2><p>some short clarifying text</p></div>
  <div class="abs nav-item" style="left:315px"><h2>Hosting.</h2><p>some short clarifying text</p></div>
  <div class="abs nav-item" style="left:591px"><h2>Services.</h2><p>some short clarifying text</p></div>
  <div class="abs server-photo" role="img" aria-label="Photo of a black server rack chassis"></div>
</header>

<section class="abs plans">
  <div class="plan"><h3><i>Advanced</i> Plan</h3><p>full service solution</p>
    <span class="order">Order <svg viewBox="0 0 20 20"><circle cx="10" cy="10" r="8" fill="none" stroke="#888" stroke-width="1.5"/><path d="M8 6l4 4-4 4" fill="none" stroke="#888" stroke-width="1.5"/></svg></span></div>
  <div class="plan"><h3><i>Business</i> Plan</h3><p>full service solution</p>
    <span class="order">Order <svg viewBox="0 0 20 20"><circle cx="10" cy="10" r="8" fill="none" stroke="#888" stroke-width="1.5"/><path d="M8 6l4 4-4 4" fill="none" stroke="#888" stroke-width="1.5"/></svg></span></div>
  <div class="plan" style="border-bottom:none"><h3><i>Standard</i> Plan</h3><p>full service solution</p>
    <span class="order">Order <svg viewBox="0 0 20 20"><circle cx="10" cy="10" r="8" fill="none" stroke="#888" stroke-width="1.5"/><path d="M8 6l4 4-4 4" fill="none" stroke="#888" stroke-width="1.5"/></svg></span></div>
</section>

<main class="abs center">
  <div class="feature"><div class="thumb" role="img" aria-label="Mobile phone"></div><p>Lorem ipsum dolor sit amet,<br>consectetuer adipiscing elit. Vivamus</p></div>
  <div class="feature"><div class="thumb" role="img" aria-label="Desktop server tower"></div><p>Lorem ipsum dolor sit amet,<br>consectetuer adipiscing elit. Vivamus</p></div>
  <div class="feature"><div class="thumb" role="img" aria-label="Leather wallet"></div><p>Lorem ipsum dolor sit amet,<br>consectetuer adipiscing elit. Vivamus</p></div>
  <div class="news">
    <h3>Company News</h3>
    <div class="date">March 12, 2003, Saturday</div>
    <h4>QH announces new Valdex rack</h4>
    <p>Vestibulum ante ipsum primis in faucibus orci luctus et ultrices posuere cubilia Curae;</p>
  </div>
</main>

<aside class="abs upgrades">
  <h3>Recent Upgrades</h3>
  <div class="sub">ON OUR SERVER TECHNICAL SITE</div>
  <div class="rack" role="img" aria-label="Rack-mounted server unit"></div>
  <p class="body">Lorem ipsum dolor sit amet, consectetuer adipiscing elit. Vivamus dolor, cursus at, volutpat fermentum, imperdiet sit amet, sapien. Pellentesque.</p>
</aside>

<section>
  <div class="abs access"><h3>Customer Access</h3><div class="sub">some short clarifying text</div></div>
  <div class="abs lock" role="img" aria-label="Padlock"></div>
  <div class="abs field" style="top:714px">your name</div>
  <div class="abs field" style="top:754px">••••••••••••••••</div>
  <div class="abs login">log in</div>
  <div class="abs forgot">forgot your password?</div>
</section>

<nav class="abs links">
  <div class="link"><h3>Corporation's Profile</h3><p>some short clarifying text</p><svg viewBox="0 0 20 20"><circle cx="10" cy="10" r="8" fill="none" stroke="#fff" stroke-width="1.5"/><path d="M8 6l4 4-4 4" fill="none" stroke="#fff" stroke-width="1.5"/></svg></div>
  <div class="link"><h3>Featured Services</h3><p>some short clarifying text</p><svg viewBox="0 0 20 20"><circle cx="10" cy="10" r="8" fill="none" stroke="#fff" stroke-width="1.5"/><path d="M8 6l4 4-4 4" fill="none" stroke="#fff" stroke-width="1.5"/></svg></div>
  <div class="link" style="border-bottom:none"><h3>Hot Offer</h3><p>some short clarifying text</p><svg viewBox="0 0 20 20"><circle cx="10" cy="10" r="8" fill="none" stroke="#fff" stroke-width="1.5"/><path d="M8 6l4 4-4 4" fill="none" stroke="#fff" stroke-width="1.5"/></svg></div>
</nav>

<footer class="abs footer">
  <div>Copyright 2006. &nbsp; Legal Notice &nbsp; | &nbsp; Terms of Use / Privacy Policy<small>www.quorinnetworks.com</small></div>
  <nav><span>Home.</span><span>Hosting.</span><span>Services.</span><span>Support.</span><span>Contacts.</span></nav>
</footer>

</body>
</html>
```